Business Card Design needed for logo design project

Would like a professional business card for a company involved in financial and latest technologies including CAD design. We would like the card to convey professionalism and communicate that we are involved in up to date technology solutions.

Target Market(s)

Business 2 Business sales

Industry/Entity Type

Financial

Colors

Designer to choose colors to be used in the design.

Requirements
Must have
• Business Name
Logo
Name
Phone
Email
Nice to have
• Website

```html
<!DOCTYPE html>
<html lang="en">
<head>
<meta charset="utf-8">
<title>Business Card – Front and Back</title>
<link rel="stylesheet" href="https://fonts.googleapis.com/css2?family=Source+Sans+3:wght@400;600&display=swap">
<style>
  :root {
    --navy: #062231;
    --stone: #b1b1b0;
    --ghost: #c0c0bf;
    --page: #f3f3f3;
    --shadow: rgba(0, 0, 0, 0.35);
  }
  * { margin: 0; padding: 0; box-sizing: border-box; }
  html, body {
    width: 1152px;
    height: 1200px;
    overflow: hidden;
    background: var(--page);
    font-family: "Source Sans 3", "Myriad Pro", Arial, sans-serif;
  }
  .canvas {
    position: relative;
    width: 1152px;
    height: 1200px;
  }
  .card {
    position: absolute;
    left: 181px;
    width: 740px;
    height: 430px;
    overflow: hidden;
    box-shadow: 5px 5px 7px var(--shadow);
  }
  .card__swoosh {
    position: absolute;
    inset: 0;
    width: 100%;
    height: 100%;
  }

  /* Front */
  .card--front {
    top: 81px;
    background: var(--navy);
  }
  .card--front .card__swoosh path { fill: var(--stone); }
  .brand-name {
    position: absolute;
    inset: 0 0 10px 0;
    display: flex;
    flex-direction: column;
    align-items: center;
    justify-content: center;
    color: #ffffff;
    font-size: 100px;
    font-weight: 400;
    line-height: 80px;
    letter-spacing: 1px;
    text-align: center;
  }

  /* Back */
  .card--back {
    top: 737px;
    background: var(--stone);
  }
  .card--back .card__swoosh path { fill: var(--navy); }
  .brand-echo {
    position: absolute;
    left: 378px;
    top: 38px;
    color: var(--ghost);
    font-size: 42px;
    line-height: 58px;
    font-weight: 400;
  }
  .contact {
    position: absolute;
    left: 51px;
    top: 236px;
    color: var(--navy);
    font-size: 21px;
    line-height: 31px;
    list-style: none;
  }
  .contact__name { text-transform: uppercase; }
  .website {
    position: absolute;
    left: 51px;
    top: 362px;
    color: var(--navy);
    font-size: 21px;
    line-height: 31px;
  }
</style>
</head>
<body>
<main class="canvas">

  <section class="card card--front" aria-label="Business card front">
    <svg class="card__swoosh" viewBox="0 0 482 280" preserveAspectRatio="none" aria-hidden="true">
      <path d="M0 280 Q330 268 482 200 L482 280 Z"/>
    </svg>
    <h1 class="brand-name"><span>LOGO</span><span>NAME</span></h1>
  </section>

  <section class="card card--back" aria-label="Business card back">
    <svg class="card__swoosh" viewBox="0 0 482 280" preserveAspectRatio="none" aria-hidden="true">
      <path d="M0 280 Q330 266 482 200 L482 280 Z"/>
    </svg>
    <p class="brand-echo">logo name<br>repeated<br>in transparency</p>
    <ul class="contact">
      <li class="contact__name">Marlow Fenn</li>
      <li class="contact__phone">+39 3201987764</li>
      <li class="contact__email">marlowfenn@mailbox.net</li>
    </ul>
    <p class="website">www.marlowfenn.net</p>
  </section>

</main>
</body>
</html>
```